TARPLOAD business card design

TARPLOAD is a manufacturer of skip bags supplying both the domestic and commercial market. We wish to convey core characteristics of strength, professionalism and reliability to our customers. We are after a business card that uses our company colours of black and yellow as well as incorporating our logo. Our customers are predominantly in the construction or hardware industry. It is important the cards are professional as we are a small company wishing to appear larger than we actually are. more info on the company and product available at www.tarpload-example.com.au

Target Market(s)

hardware buyers, contruction company owners

Industry/Entity Type

Construction

Requirements
Must have
• company colours of black and yellow - No other colours or variation of yellow black. our company logo. card design must convey "tough"
• Card design must be landscape
• Details to be included on the card are:
• Name and Tiltle
• Phone number : 1300 41 62 53
• Mobile: 0452 718 903
• Fax: 03 9617 4852
• email: dale.hendry@tarpload-example.com.au
• address: PO Box 517, Kelvindale, VIC,3294
• Text in white when on a black background
Nice to have
• I like the idea of the back of the card being black with lighter circle area in the middle with black logo in the centre. Similar to the attached "iconic" card

```html
<!DOCTYPE html>
<html lang="en">
<head>
<meta charset="utf-8">
<title>TARPLOAD business card concepts</title>
<link rel="stylesheet" href="https://fonts.googleapis.com/css2?family=Anton&family=Arimo:wght@700&display=swap">
<style>
  :root {
    --yellow: #f2c500;
    --yellow-glow: #fff3c4;
    --yellow-mid: #f9dc63;
    --black: #000000;
    --white: #ffffff;
    --page: #ffffff;
    --condensed: "Anton", "Impact", sans-serif;
    --grotesk: "Arimo", "Helvetica Neue", Arial, sans-serif;
  }
  html, body {
    margin: 0;
    padding: 0;
    width: 1200px;
    height: 693px;
    overflow: hidden;
    background: var(--page);
  }
  .sheet {
    position: relative;
    width: 1200px;
    height: 693px;
  }
  .card {
    position: absolute;
    top: 236px;
    width: 364px;
    height: 222px;
    background: var(--yellow);
    overflow: hidden;
  }
  .card--condensed { left: 30px; }
  .card--back {
    left: 418px;
    background: radial-gradient(ellipse at 50% 50%, var(--yellow-glow) 0, var(--yellow-mid) 70px, var(--yellow) 150px);
  }
  .card--grotesk { left: 806px; }

  .line { position: absolute; left: 0; width: 100%; margin: 0; text-align: center; white-space: nowrap; }
  .contact { position: absolute; margin: 0; padding: 0; list-style: none; white-space: nowrap; }

  /* Condensed card */
  .card--condensed .brand-name {
    position: absolute; left: 18px; top: 10px; margin: 0;
    font-family: var(--condensed); font-size: 26px; line-height: 34px;
    color: var(--black); letter-spacing: 1px;
  }
  .card--condensed .name-band {
    position: absolute; left: 0; top: 50px; width: 100%; height: 40px;
    background: var(--black);
  }
  .card--condensed .person-name {
    top: 50px; font-family: var(--condensed); font-weight: 400; font-size: 27px; line-height: 40px;
    color: var(--white); letter-spacing: 0.5px;
  }
  .card--condensed .role {
    top: 96px; font-family: var(--condensed); font-size: 14px; line-height: 20px; color: var(--black);
  }
  .card--condensed .contact {
    left: 26px; top: 126px;
    font-family: var(--condensed); font-size: 13px; line-height: 22px; color: var(--black); letter-spacing: 0.3px;
  }
  .card--condensed .details {
    position: absolute; right: 22px; top: 126px; margin: 0; text-align: right; white-space: nowrap;
    font-family: var(--condensed); font-size: 12.5px; line-height: 22px; color: var(--black); letter-spacing: 0.2px;
  }

  /* Back card */
  .card--back .brand-name {
    top: 0; font-family: var(--condensed); font-size: 64px; line-height: 222px;
    color: var(--black); letter-spacing: 1px;
  }

  /* Grotesk card */
  .card--grotesk .name-band {
    position: absolute; left: 0; top: 20px; width: 100%; height: 42px;
    background: var(--black);
  }
  .card--grotesk .person-name {
    top: 20px; font-family: var(--grotesk); font-weight: 700; font-size: 30px; line-height: 42px;
    color: var(--yellow); letter-spacing: 0.5px;
  }
  .card--grotesk .role {
    top: 68px; font-family: var(--grotesk); font-weight: 700; font-size: 15px; line-height: 22px;
    color: var(--black); letter-spacing: 0.4px;
  }
  .card--grotesk .contact {
    left: 112px; top: 96px;
    font-family: var(--grotesk); font-weight: 700; font-size: 13px; line-height: 19px;
    color: var(--black); letter-spacing: 0.8px;
  }
  .card--grotesk .details {
    top: 160px; font-family: var(--grotesk); font-weight: 700; font-size: 11.5px; line-height: 17px;
    color: var(--black); letter-spacing: 0.2px;
  }

  .caption {
    position: absolute; top: 478px; width: 364px; margin: 0; text-align: center;
    font-family: var(--grotesk); font-weight: 700; font-size: 15px; color: var(--black);
  }
  .caption--condensed { left: 30px; }
  .caption--grotesk { left: 806px; }
</style>
</head>
<body>
<main class="sheet">

  <section class="card card--condensed" aria-label="Front, condensed type">
    <p class="brand-name">TARPLOAD</p>
    <div class="name-band"></div>
    <h1 class="line person-name">Dale Hendry</h1>
    <p class="line role">Managing Director</p>
    <ul class="contact">
      <li>P&nbsp; : 1300 41 62 53</li>
      <li>M : 0452 718 903</li>
      <li>F&nbsp; : 03 9617 4852</li>
    </ul>
    <p class="details">PO Box 517, Kelvindale, VIC, 3294<br>dale.hendry@tarpload-example.com.au<br>www.tarpload-example.com.au</p>
  </section>

  <section class="card card--back" aria-label="Back">
    <p class="line brand-name">TARPLOAD</p>
  </section>

  <section class="card card--grotesk" aria-label="Front, grotesk type">
    <div class="name-band"></div>
    <h1 class="line person-name">Dale Hendry</h1>
    <p class="line role">Managing Director</p>
    <ul class="contact">
      <li>P&nbsp; : 1300 41 62 53</li>
      <li>M : 0452 718 903</li>
      <li>F&nbsp;&nbsp; : 03 9617 4852</li>
    </ul>
    <p class="line details">PO Box 517, Kelvindale, VIC, 3294<br>dale.hendry@tarpload-example.com.au<br>www.tarpload-example.com.au</p>
  </section>

  <p class="caption caption--condensed">Font 1: Haettenschweiler</p>
  <p class="caption caption--grotesk">Font 2: Helvetica Neue</p>

</main>
</body>
</html>
```